MiniGolfPubCrawl

Looking to get a poster design for We do a pub crawl/ mini golf tournament. There is one hole set up at 15+ bars.
We want this to have a golf theme, but also a party theme. Want it to look like an event / band poster.
Stuff that needs to be included:
Riverbend Pintstack Cup #5- "a mini golf tournament, but more importantly a pub crawl"
Cost- $155 per 4 some
Sat Nov 23rd- Noon Start- After Party at Vex- 430
Holes set up at bars all over the 3rd Ward.
Lunch Included from the Crisp Wagoneer Food Truck
Tons of prizes up for grabs, ($3000+ in gift cards)
Sign Up today at RvbPintstackCup.com
Drink Specials all day at all bars
okay i'm having trouble attaching files as to some posters I like so here are some links;
http://brightpinelakesidefestival.org/wp-content/uploads/2013/01/BPLFPrintablePosterScreenshot.jpg
http://runnersforhope.files.examplepress.com/2012/06/2012-tz7h-poster-600lr.jpg?w=625
http://rowingtogether.files.examplepress.com/2011/02/screen-shot-2011-02-21-at-9-09-08-am.png

```html
<!DOCTYPE html>
<html lang="en">
<head>
<meta charset="utf-8">
<title>Riverbend Pintstack Cup #5</title>
<link rel="stylesheet" href="https://fonts.googleapis.com/css2?family=Rubik+Dirt&family=Oswald:wght@500;600&display=swap">
<style>
  :root {
    --cyan-glow: #7ff0f6;
    --teal: #1aa6b5;
    --teal-deep: #0b4f5c;
    --edge: #06242c;
    --lime: #c6e44a;
    --grass: #5f9f2c;
    --navy: #1c2c55;
    --panel: #1d2236;
    --ink: #ffffff;
    --silhouette: #0d1712;
  }
  * { margin: 0; padding: 0; box-sizing: border-box; }
  html, body { width: 800px; height: 1200px; overflow: hidden; background: var(--edge); }
  .poster {
    position: relative;
    width: 800px;
    height: 1200px;
    overflow: hidden;
    color: var(--ink);
    font-family: "Oswald", "Arial Narrow", sans-serif;
    background:
      radial-gradient(ellipse 420px 380px at 400px 330px, var(--cyan-glow) 0%, rgba(60,200,215,.6) 45%, rgba(0,0,0,0) 100%),
      radial-gradient(ellipse 520px 420px at 400px 900px, var(--lime) 0%, var(--grass) 55%, rgba(20,60,40,0) 100%),
      linear-gradient(180deg, var(--teal-deep) 0%, var(--teal) 35%, #2a9a8a 60%, #1d4a32 100%);
  }
  .poster::before {
    content: "";
    position: absolute;
    inset: 0;
    background: repeating-conic-gradient(from 0deg at 400px 880px, rgba(255,255,255,.09) 0deg 5deg, rgba(255,255,255,0) 5deg 12deg);
  }
  .poster::after {
    content: "";
    position: absolute;
    inset: 0;
    background: radial-gradient(ellipse 560px 720px at 400px 560px, rgba(0,0,0,0) 55%, rgba(2,20,26,.75) 100%);
    pointer-events: none;
  }
  .hill { position: absolute; left: 0; top: 840px; width: 800px; height: 360px; }
  .title {
    position: absolute;
    left: 0; right: 0;
    text-align: center;
    white-space: nowrap;
    font-family: "Rubik Dirt", "Impact", sans-serif;
    font-weight: 400;
    line-height: 1;
    z-index: 2;
    text-shadow: 0 3px 6px rgba(0,0,0,.35);
  }
  .title-line1 { top: 62px; font-size: 102px; letter-spacing: 1px; }
  .title-line2 { top: 154px; font-size: 84px; letter-spacing: -1px; }
  .edition { top: 244px; font-size: 180px; transform: skewX(-8deg); }
  .tagline {
    position: absolute; top: 458px; left: 0; right: 0;
    text-align: center; font-size: 26px; font-weight: 500; letter-spacing: .5px; z-index: 2;
    white-space: nowrap;
  }
  .date-box {
    position: absolute; left: 236px; top: 530px; width: 310px; height: 150px; z-index: 2;
  }
  .date-box svg { position: absolute; inset: 0; width: 100%; height: 100%; }
  .date-text { position: relative; text-align: center; padding-top: 14px; line-height: 1.15; }
  .date-main { font-size: 46px; font-weight: 600; }
  .date-sub { font-size: 32px; font-weight: 500; }
  .side-note {
    position: absolute; z-index: 2; text-align: center; line-height: 1.2;
    transform: rotate(-8deg); text-shadow: 0 2px 4px rgba(0,0,0,.4);
    white-space: nowrap;
  }
  .after-party { left: 28px; top: 556px; width: 230px; font-size: 42px; font-weight: 500; }
  .drink-specials { left: 556px; top: 552px; width: 220px; font-size: 30px; font-weight: 500; }
  .golfer {
    position: absolute; left: 330px; top: 675px; width: 160px; height: 335px; z-index: 1;
    background: linear-gradient(180deg, var(--silhouette) 0%, #1a2a1c 100%);
    border-radius: 80px 80px 40px 40px;
  }
  .headline {
    position: absolute; left: 0; right: 0; text-align: center; z-index: 3;
    text-shadow: 0 2px 6px rgba(0,0,0,.5); font-weight: 500; white-space: nowrap;
  }
  .holes { top: 732px; font-size: 44px; }
  .lunch { top: 808px; font-size: 34px; }
  .prizes {
    position: absolute; left: 18px; top: 892px; width: 186px; height: 170px; z-index: 3;
    background: var(--panel); border: 2px solid rgba(255,255,255,.35);
    transform: rotate(-8deg); text-align: center; font-size: 24px; line-height: 1.3;
    padding-top: 10px; font-weight: 500; box-shadow: 0 4px 12px rgba(0,0,0,.5);
  }
  .cost {
    position: absolute; left: 582px; top: 958px; width: 172px; height: 172px; z-index: 3;
    border-radius: 50%; background: radial-gradient(circle, #1e2a4c 0%, #141b33 100%);
    border: 2px solid rgba(160,190,230,.4); box-shadow: 0 4px 14px rgba(0,0,0,.6);
    display: flex; align-items: center; justify-content: center;
  }
  .cost-text { transform: rotate(-14deg); text-align: center; font-size: 30px; line-height: 1.2; font-weight: 500; white-space: nowrap; }
  .signup {
    position: absolute; left: 30px; top: 1138px; z-index: 3; font-size: 31px; font-weight: 500; white-space: nowrap;
  }
</style>
</head>
<body>
<main class="poster">
  <svg class="hill" viewBox="0 0 800 360" aria-hidden="true">
    <defs>
      <radialGradient id="hillShade" cx="50%" cy="10%" r="80%">
        <stop offset="0" stop-color="#2b4a22"/>
        <stop offset=".5" stop-color="#13241a"/>
        <stop offset="1" stop-color="#070d0a"/>
      </radialGradient>
    </defs>
    <path d="M0 90 Q400 -60 800 90 L800 360 L0 360 Z" fill="url(#hillShade)"/>
  </svg>

  <h1 class="title title-line1">RIVERBEND</h1>
  <h1 class="title title-line2">PINTSTACK CUP</h1>
  <div class="title edition">#5</div>

  <p class="tagline">"a mini golf tournament, but more importantly a pub crawl"</p>

  <div class="side-note after-party">After Party<br>at Vex- 430</div>

  <div class="date-box">
    <svg viewBox="0 0 310 150" preserveAspectRatio="none" aria-hidden="true">
      <defs>
        <linearGradient id="dateFill" x1="0" y1="0" x2="0" y2="1">
          <stop offset="0" stop-color="#24386a"/>
          <stop offset="1" stop-color="#2f5698"/>
        </linearGradient>
      </defs>
      <polygon points="6,8 310,0 294,150 18,142" fill="url(#dateFill)"/>
    </svg>
    <div class="date-text">
      <div class="date-main">Sat Nov 23rd</div>
      <div class="date-sub">Noon Start</div>
    </div>
  </div>

  <div class="side-note drink-specials">Drink Specials all<br>day at all bars</div>

  <div class="golfer" role="img" aria-label="Silhouette of a golfer finishing a swing"></div>

  <p class="headline holes">Holes set up at bars all over the 3rd Ward.</p>
  <p class="headline lunch">Lunch Included from the Crisp Wagoneer Food Truck</p>

  <div class="prizes">Tons of prizes<br>up for grabs<br>($3000+<br>in gift cards)</div>

  <div class="cost"><div class="cost-text">Cost- $155<br>per 4 some</div></div>

  <p class="signup">Sign Up today at RvbPintstackCup.com</p>
</main>
</body>
</html>
```